Redesign of an existing homepage

This site needs a redesign
https://www.ferien-am-haldbach.de
This page with the accommodation options is important for the customer
https://www.ferien-am-haldbach.de/gastgeber/
Till now there is a new logo. See attachment. That's all I have.
It would make sense to use the colors of the logo in the redesign.
footer.jpg.
I would put this info into the footer. The graphic (Infomaterial) is not needed.
a new menu - links.jpg
This info can be put in a new menu. Therefore the right column is gone and there is more space for the design.
NEW:
Please keep in mind that the Icons are important and shall be displayed under every accommodation
Number of Pages Required
1 page

```html
<!DOCTYPE html>
<html lang="de">
<head>
<meta charset="utf-8">
<title>Ferienverband Haldbach – Urlaub im Haldtal</title>
<link href="https://fonts.googleapis.com/css2?family=Poppins:ital,wght@0,400;0,500;0,600;1,400;1,500&display=swap" rel="stylesheet">
<style>
:root{
  --blue:#1a6fb5;
  --sky:#27a2db;
  --green:#79b41e;
  --text:#333a40;
  --muted:#5b6570;
  --line:#ece8d8;
  --panel:#f4f8e6;
  --white:#ffffff;
}
*{box-sizing:border-box;margin:0;padding:0}
html,body{width:1200px;height:3682px;overflow:hidden}
body{position:relative;font-family:'Poppins',sans-serif;color:var(--text);background:var(--white)}
.abs{position:absolute}
a{text-decoration:none;color:inherit}

/* top bar */
.topbar{left:0;top:0;width:1200px;height:33px;background:var(--blue);color:var(--green);font-size:14px}
.topbar .phone{left:66px;top:7px;display:flex;gap:16px;align-items:center}
.topbar .mail{right:62px;top:7px;display:flex;gap:14px;align-items:center}

/* nav */
.nav{left:0;top:33px;width:1200px;height:71px;background:var(--white);font-size:14px;color:var(--blue)}
.nav a{position:absolute;top:27px}
.nav a.active{color:var(--green)}
.brand{left:500px;top:0;width:200px;text-align:center}
.brand .dot{width:50px;height:50px;border-radius:50%;background:var(--green);margin:-26px auto 4px;border:3px solid var(--white)}
.brand .name{font-size:13px;font-weight:600;color:var(--blue);line-height:14px}

/* hero */
.hero{left:0;top:104px;width:1200px;height:646px;overflow:hidden;background:linear-gradient(180deg,#3d4a3a 0%,#566c3e 45%,#4f6a30 80%,#3c5524 100%)}
.hero-photo{position:absolute;inset:0;background:radial-gradient(ellipse at 52% 45%,rgba(160,140,120,.45),rgba(0,0,0,0) 55%)}
.hero h1{position:absolute;left:0;width:1200px;top:160px;text-align:center;font-weight:600;font-size:56px;line-height:48px;letter-spacing:1px}
.hero h1 .l1{color:var(--green);display:block}
.hero h1 .l2{color:var(--sky);display:block;font-weight:500}
.hero p{position:absolute;left:390px;width:420px;top:278px;text-align:center;color:var(--white);font-size:14px;line-height:20px}
.btn{position:absolute;display:flex;align-items:center;justify-content:center;border-radius:10px;font-weight:500;font-size:15px;color:var(--white)}
.hero .btn{left:518px;top:339px;width:164px;height:37px;background:var(--blue)}
.hero-curve{position:absolute;left:0;bottom:0}

/* partners */
.partners{left:0;top:750px;width:1200px;height:100px}
.badge{position:absolute;top:0}

/* section titles */
.section-title{position:absolute;left:0;width:1200px;text-align:center;color:var(--sky);font-weight:500;font-size:31px}

/* hosts */
.host-photo{position:absolute;width:354px;height:354px;border-radius:50%}
.host-body{position:absolute;width:440px}
.host-body h3{color:var(--blue);font-size:19px;font-weight:600}
.host-body .addr{color:var(--sky);font-size:11px;margin-top:3px}
.host-body .desc{font-size:12.5px;line-height:19.5px;color:var(--text);margin-top:7px}
.amenities{display:flex;gap:3.5px;margin-top:12px}
.amenities span{width:17px;height:17px;border:1.3px solid #222;border-radius:2px;font-size:10px;font-weight:600;line-height:14px;text-align:center;color:#222;display:flex;align-items:center;justify-content:center}
.amenities span i{display:block;width:8px;height:6px;border:1.3px solid #222;border-radius:1px}
.price{color:var(--green);font-style:italic;font-size:13px;margin-top:12px}
.host-body .btn{position:relative;margin-top:14px;width:414px;height:37px;background:var(--blue);font-size:15px}
.divider{position:absolute;left:57px;width:1083px;height:1px;background:var(--line)}

/* more */
.btn.more{left:518px;top:2185px;width:164px;height:37px;background:var(--green)}

/* info */
.info-card{position:absolute;width:525px;height:268px;background:var(--panel);border-radius:16px}
.info-card .cover{position:absolute;left:16px;top:14px;width:226px;height:240px}
.info-card .txt{position:absolute;left:262px;right:20px;top:0;height:100%;display:flex;flex-direction:column;justify-content:center;align-items:center;text-align:center}
.info-card h4{color:var(--blue);font-size:18px;font-weight:500;line-height:24px}
.info-card .read{margin-top:10px;color:var(--green);font-style:italic;font-size:14px;text-decoration:underline}

/* footer */
.footer-wave{left:0;top:3250px}
.footer{left:0;top:3330px;width:1200px;height:352px;background:var(--blue);color:var(--white)}
.events{left:289px;top:3009px;width:622px;height:344px;background:var(--white);border-radius:14px;box-shadow:0 4px 16px rgba(0,0,0,.08)}
.events h2{position:absolute;left:0;width:100%;top:40px;text-align:center;color:var(--sky);font-weight:500;font-size:31px}
.events .photo{position:absolute;left:50px;top:100px;width:218px;height:218px;border-radius:50%;background:radial-gradient(circle at 50% 40%,#b9852f,#6f6a2c 60%,#4d5a24)}
.events h4{position:absolute;left:306px;top:168px;width:270px;color:var(--blue);font-weight:600;font-size:18px;line-height:24px}
.events .btn{left:306px;top:224px;width:165px;height:37px;background:var(--green)}

.fcol{position:absolute;text-align:center}
.fcol h5{color:var(--green);font-weight:500;font-size:19px}
.ficon{width:36px;height:36px;border-radius:50%;border:1.5px solid var(--white);margin:0 auto;display:flex;align-items:center;justify-content:center}
.fsmall{font-size:13px}
.vline{position:absolute;top:3430px;width:1px;height:170px;background:rgba(255,255,255,.35)}
.hours{display:grid;grid-template-columns:82px auto;font-size:13px;row-gap:6px;text-align:left;margin-top:10px}
.foot-line{position:absolute;left:57px;top:3638px;width:1083px;height:1px;background:rgba(255,255,255,.35)}
.copy{position:absolute;left:0;width:1200px;top:3654px;text-align:center;color:var(--white);font-size:12.5px}
</style>
</head>
<body>

<header>
  <div class="abs topbar">
    <div class="abs phone">
      <svg width="18" height="18" viewBox="0 0 24 24"><path fill="#79b41e" d="M6.6 10.8a15 15 0 0 0 6.6 6.6l2.2-2.2c.3-.3.7-.4 1-.2 1.1.4 2.3.6 3.6.6.6 0 1 .4 1 1V20c0 .6-.4 1-1 1A17 17 0 0 1 3 4c0-.6.4-1 1-1h3.5c.6 0 1 .4 1 1 0 1.3.2 2.5.6 3.6.1.3 0 .7-.2 1z"/></svg>
      <span>+ 0100 200 300</span>
    </div>
    <div class="abs mail">
      <svg width="18" height="14" viewBox="0 0 18 14"><rect width="18" height="14" rx="1.5" fill="#79b41e"/><path d="M1 1.5l8 6 8-6" stroke="#1a6fb5" stroke-width="1.6" fill="none"/></svg>
      <span>info@ferien-am-haldbach.de</span>
    </div>
  </div>
  <nav class="abs nav">
    <a class="active" style="left:61px">Home</a>
    <a style="left:136px">Gastgeber</a>
    <a style="left:239px">Haldtal</a>
    <a style="left:309px">Freizeit</a>
    <div class="abs brand">
      <div class="dot"></div>
      <div class="name">FERIENVERBAND<br>HALDBACH</div>
    </div>
    <a style="left:850px">Ausflugsziele</a>
    <a style="left:967px">Kunst &amp; Kultur</a>
    <a style="left:1090px">kontakt</a>
  </nav>
</header>

<section class="abs hero">
  <div class="hero-photo" role="img" aria-label="Familienfoto: Eltern mit Kind sitzen lachend auf einer Wiese"></div>
  <h1><span class="l1">Urlaub im Haldtal - dem</span><span class="l2">schönsten Fleck Bayerns</span></h1>
  <p>Kultur und Natur, Lebensfreude und Genuss, freundliche und aufgeschlossene Menschen...</p>
  <a class="btn">Contact Us</a>
  <svg class="hero-curve" width="1200" height="110" viewBox="0 0 1200 110"><path d="M0 110 Q600 -80 1200 110Z" fill="#fff"/></svg>
</section>

<section class="abs partners" aria-label="Partner">
  <div class="badge" style="left:255px;width:84px;height:84px;border-radius:50%;background:#3bb0c9"></div>
  <div class="badge" style="left:433px;top:28px;width:132px;height:30px;border-radius:4px;background:#d9dde2"></div>
  <div class="badge" style="left:637px;width:128px;height:90px;border-radius:3px;background:#2f8f52"></div>
  <div class="badge" style="left:840px;top:28px;width:128px;height:34px;border-radius:4px;background:#c9ddef"></div>
</section>

<h2 class="section-title" style="top:915px">Gastgeber im Haldtal</h2>

<!-- host 1 -->
<article>
  <div class="host-photo" style="left:158px;top:993px;background:linear-gradient(180deg,#7e9a7a 0%,#c9b8a6 45%,#5e8a3c 75%,#476d2c 100%)" role="img" aria-label="Ferienhaus mit Holzzaun und Garten vor Nadelwald"></div>
  <div class="host-body" style="left:595px;top:1045px">
    <h3>Ferienhaus Sonnwinkel F</h3>
    <div class="addr">Lindenweg 23, 84000 Haldbach</div>
    <p class="desc">Ein exklusives Ferienhaus für Sie alleine, vom Gästeverband mit 5 Sternen ausgezeichnet, für Menschen, welche die Ruhe suchen aber auf den Komfort nicht verzichten wollen, mit offenem Kamin, W-Lan und großem eingezäunten Garten.</p>
    <div class="amenities"><span>i</span><span><i></i></span><span><i></i></span><span>⌂</span><span>✓</span><span>♨</span><span>☼</span><span><i></i></span><span>♣</span><span>≈</span><span>∿</span><span>▲</span><span>↔</span><span><i></i></span><span>⟳</span><span>P</span><span>P</span><span>⌂</span><span>W</span><span>○</span></div>
    <div class="price">ab € 90,00 für 2 Personen</div>
    <a class="btn">Zur Homepage von Ferienhaus Sonnwinkel</a>
  </div>
  <div class="divider" style="top:1347px"></div>
</article>

<!-- host 2 -->
<article>
  <div class="host-photo" style="left:687px;top:1390px;background:linear-gradient(180deg,#8fa9c4 0%,#b9c6cf 30%,#6b4a2e 55%,#8a6a4a 75%,#4f7a33 100%)" role="img" aria-label="Alpenländischer Bauernhof mit Blumenbalkonen vor Bergkulisse"></div>
  <div class="host-body" style="left:157px;top:1442px">
    <h3>Birkenhof F</h3>
    <div class="addr">Birkenau 3, 94000 Waldried</div>
    <p class="desc">In traumhaft ländlicher Kulisse, inmitten von Wald und Wiesen, finden Sie den Birkenhof zwischen Auenstadt und Bergheim, im Herzen von Niederbayern. Abseits von Hektik, Lärm und Alltagsstress lädt unser Bauernhof und Gastronomiebetrieb zum Genießen.</p>
    <div class="amenities"><span>i</span><span><i></i></span><span><i></i></span><span>⌂</span><span>✓</span><span>♨</span><span>☼</span><span><i></i></span><span>♣</span><span>≈</span><span>∿</span><span>▲</span><span>↔</span><span><i></i></span><span>⟳</span><span>P</span><span>P</span><span>⌂</span><span>W</span><span>○</span></div>
    <div class="price">Preis auf Anfrage</div>
    <a class="btn">Zur Homepage von Birkenhof</a>
  </div>
  <div class="divider" style="top:1745px"></div>
</article>

<!-- host 3 -->
<article>
  <div class="host-photo" style="left:158px;top:1789px;background:linear-gradient(180deg,#c8d9e6 0%,#9fb7c6 25%,#5f7f4a 50%,#4a6c34 80%,#3b5a28 100%)" role="img" aria-label="Hügellandschaft mit Dorf, Wiesen und Wäldern"></div>
  <div class="host-body" style="left:595px;top:1841px">
    <h3>Camp Wiesental C</h3>
    <div class="addr">Wiesenstraße 11, 94100 Auental</div>
    <p class="desc">Camping für alle Generationen. Das Camp Wiesental ist ein ideales Reiseziel für Erholungssuchende, Wellness-Freunde, Aktivurlauber sowie Familien mit Kindern. Umgeben von weiten Feldern und bewaldeten Hügeln laden gleich.</p>
    <div class="amenities"><span>i</span><span><i></i></span><span><i></i></span><span>⌂</span><span>✓</span><span>♨</span><span>☼</span><span><i></i></span><span>♣</span><span>≈</span><span>∿</span><span>▲</span><span>↔</span><span><i></i></span><span>⟳</span><span>P</span><span>P</span><span>⌂</span><span>W</span><span>○</span></div>
    <div class="price">ab € 23,90 für 2 Personen</div>
    <a class="btn">Zur Homepage von Camp Wiesental</a>
  </div>
  <div class="divider" style="top:2144px"></div>
</article>

<a class="btn more">View More</a>

<h2 class="section-title" style="top:2290px">Informationen &amp; Prospekte</h2>

<section aria-label="Prospekte">
  <div class="info-card" style="left:60px;top:2368px">
    <div class="cover" style="background:linear-gradient(180deg,#a9c7e0 0%,#7da35a 45%,#5b8a3a 85%,#6aa22a 100%)" role="img" aria-label="Titelbild Gastgeberverzeichnis: Baum und Wanderin auf Wiese"></div>
    <div class="txt"><h4>Gastgeberverzeichnis<br>Haldbach und<br>Umgebung</h4><a class="read">Read More</a></div>
  </div>
  <div class="info-card" style="left:615px;top:2368px">
    <div class="cover" style="background:linear-gradient(180deg,#d6dfe8 0%,#8a9aa8 40%,#3a3a3a 65%,#7ab51e 88%,#7ab51e 100%)" role="img" aria-label="Titelbild Sehenswertes: Pferdeskulptur vor Fahnen am Marktplatz"></div>
    <div class="txt"><h4>Haldbach<br>Sehenswertes<br>entdecken</h4><a class="read">Read More</a></div>
  </div>
  <div class="info-card" style="left:60px;top:2666px">
    <div class="cover" style="background:linear-gradient(180deg,#b8cde0 0%,#9ab0c2 40%,#7b9a5c 70%,#5e8a34 100%)" role="img" aria-label="Titelbild Freizeitmagazin: Bank mit Picknick über Landschaft"></div>
    <div class="txt"><h4>FREIZEITREGION<br>HALDTAL,<br>SOO</h4><a class="read">Read More</a></div>
  </div>
  <div class="info-card" style="left:615px;top:2666px">
    <div class="cover" style="background:linear-gradient(180deg,#a4513a 0%,#b97a64 40%,#8ba6c2 60%,#9a4a36 100%)" role="img" aria-label="Titelbild Hoftour: Backsteinmauer und Hofgebäude"></div>
    <div class="txt"><h4>Haldtaler Hoftour<br>Wir öffnen Tür<br>und Tor</h4><a class="read">Read More</a></div>
  </div>
</section>

<svg class="abs footer-wave" width="1200" height="82" viewBox="0 0 1200 82"><path d="M0 62 Q600 -20 1200 20 L1200 82 L0 82Z" fill="#1a6fb5"/></svg>

<footer class="abs footer">
  <div class="fcol" style="left:90px;top:102px;width:290px">
    <h5>Contact Us</h5>
    <div class="ficon" style="margin-top:10px"><svg width="16" height="16" viewBox="0 0 24 24"><path fill="#fff" d="M6.6 10.8a15 15 0 0 0 6.6 6.6l2.2-2.2c.3-.3.7-.4 1-.2 1.1.4 2.3.6 3.6.6.6 0 1 .4 1 1V20c0 .6-.4 1-1 1A17 17 0 0 1 3 4c0-.6.4-1 1-1h3.5c.6 0 1 .4 1 1 0 1.3.2 2.5.6 3.6.1.3 0 .7-.2 1z"/></svg></div>
    <p class="fsmall" style="margin-top:10px;word-spacing:2px">+ 08500 / 123 4560 &nbsp;&nbsp; + 08500 / 123 4569</p>
    <div class="ficon" style="margin-top:12px"><svg width="16" height="12" viewBox="0 0 18 14"><rect width="18" height="14" rx="1.5" fill="#fff"/><path d="M1 1.5l8 6 8-6" stroke="#1a6fb5" stroke-width="1.6" fill="none"/></svg></div>
    <p class="fsmall" style="margin-top:10px;font-size:14px">info@ferien-am-haldbach.de</p>
  </div>
  <div class="fcol" style="left:470px;top:128px;width:260px">
    <div style="width:62px;height:62px;border-radius:50%;background:#79b41e;margin:0 auto 10px"></div>
    <div style="font-weight:600;font-size:17px;line-height:20px">FERIENVERBAND<br>HALDBACH</div>
    <p class="fsmall" style="margin-top:12px;line-height:20px">Marktplatz 1<br>84000 Haldbach</p>
  </div>
  <div class="fcol" style="left:880px;top:102px;width:170px">
    <h5>Opening hours</h5>
    <div class="hours"><span>Mon–Thurs</span><span>9:00 – 16:00</span><span>Fri</span><span>9:00 – 12:30</span></div>
  </div>
</footer>
<div class="vline" style="left:417px"></div>
<div class="vline" style="left:783px"></div>
<div class="foot-line"></div>
<p class="copy">© Ferienverbandhaldbach. All rights reserved</p>

<section class="abs events">
  <h2>Veranstaltungen</h2>
  <div class="photo" role="img" aria-label="Wandergruppe auf einem herbstlichen Waldweg"></div>
  <h4>Veranstaltungen, Hinweise und Neuigkeiten</h4>
  <a class="btn">Read More</a>
</section>

</body>
</html>
```